Web Design for Cedarfield Yard Crew

Cedarfield Yard Crew needs the photoshop files for a simple, clean and professional web design. I need a home and subpage design, although they can be very similar. See pagestridelab.com for a desired layout, although I'd like to see more design than shown on that site. The goal of the site is to attract both lawn maintenance/landscape customers and build a partner network of consultants that serve the US market. The following are needed:

- home and subpage design
- page: Home, Services, Locations, Consultants, FAQ, Contact
- if subpages have header photo, need to include 5 different header photos for each page
- favicon
Updates

I'll award the design based on the homepage concept. The minor subpage changes and other elements can be worked out in the workroom stage. Thanks, Reid

Industry/Entity Type

It Professional

```html
<!DOCTYPE html>
<html lang="en">
<head>
<meta charset="utf-8">
<title>Cedarfield Yard Crew</title>
<link rel="stylesheet" href="https://fonts.googleapis.com/css2?family=Arimo:ital,wght@0,400;0,700;1,700&family=Montserrat:wght@400;500;700&display=swap">
<style>
:root{
  --green:#6cbf1e;
  --green-dark:#4e9a10;
  --green-light:#8fd631;
  --lime:#a8d22a;
  --ink:#555759;
  --nav:#5a5b5d;
  --band:#6a6b6d;
  --footer:#4d4e50;
  --pale:#e9eaea;
  --white:#ffffff;
}
*{box-sizing:border-box;margin:0;padding:0}
html,body{width:946px;height:1200px;overflow:hidden}
body{position:relative;background:var(--white);font-family:"Arimo",Arial,sans-serif;color:var(--ink)}
.abs{position:absolute}

.site-header{left:0;top:0;width:946px;height:86px;background:linear-gradient(#fafafa,#eeeeee)}
.brand{left:74px;top:26px;display:flex;align-items:center;gap:10px}
.brand-mark{width:30px;height:30px;border:3px solid #6a6b6d;border-radius:5px}
.brand-name{font-family:"Montserrat",sans-serif;font-weight:500;font-size:20px;color:#6a6b6d;letter-spacing:.3px}
.social-top{right:80px;top:12px;display:flex;gap:4px}
.social-top span{width:20px;height:20px;border-radius:50%;background:var(--green)}
.phone{right:80px;top:48px;font-weight:700;font-style:italic;font-size:18px;color:#6a6b6d}

.main-nav{left:0;top:86px;width:946px;height:34px;background:var(--nav);display:flex;align-items:center;padding-left:74px}
.main-nav a{font-family:"Montserrat",sans-serif;font-size:11px;color:#f1f1f1;text-decoration:none;padding:0 22px;border-right:1px dotted #8a8b8d;line-height:10px}
.main-nav a:last-child{border:none}
.main-nav a.active{background:var(--green);height:40px;line-height:40px;margin-top:6px;font-weight:700;border:none;padding:0 16px;margin-right:12px}

.gallery{left:0;top:133px;width:946px;height:293px;background:var(--pale)}
.photo{position:absolute}
.promo{position:absolute;left:362px;top:207px;width:300px;height:86px;background:#9c9fa1;padding:10px 0 0 100px;font-weight:700;line-height:1}
.promo .l1{font-size:28px;color:#4b4c4e}
.promo .l2{font-size:18px;color:var(--lime);margin-top:2px}
.promo .l3{font-size:17px;color:#4b4c4e;margin-top:2px}

.slider-dots{left:448px;top:460px;display:flex;gap:2px}
.slider-dots span{width:13px;height:13px;background:var(--green-dark)}
.slider-dots span:first-child{background:var(--lime)}

.service-btn{position:absolute;top:510px;height:48px;width:210px;border-radius:24px;background:linear-gradient(var(--green-light),var(--green-dark));box-shadow:0 3px 4px rgba(0,0,0,.25);display:flex;align-items:center;padding-left:22px;gap:10px;color:#fff;font-weight:700;font-size:18px}

.about{left:0;top:585px;width:946px;height:290px;background:var(--band);border-top:3px solid var(--green)}
.about h1{position:absolute;left:76px;top:40px;font-size:29px;color:#fff;font-weight:700}
.about p{position:absolute;left:76px;width:482px;font-size:11.2px;line-height:13.6px;color:#f2f2f2}
.about p b{font-size:12.5px}

.contact-card{left:588px;top:642px;width:278px;height:251px;border-radius:4px;background:linear-gradient(var(--green-light),var(--green-dark));padding-top:18px}
.contact-card h2{text-align:center;color:#fff;font-size:24px;font-weight:700;padding-bottom:8px;border-bottom:3px double #e9f6d8;margin:0 10px 20px}
.field{display:block;width:214px;height:32px;margin:0 0 8px 32px;border:1px solid #d5efb0;border-radius:3px;color:#fff;font-size:11px;padding-left:14px;line-height:30px}
.submit{display:block;width:214px;height:35px;margin:14px 0 0 33px;background:linear-gradient(#5b5c5e,#3a3b3d);color:#fff;font-weight:700;font-size:16px;text-align:center;line-height:35px;border-radius:2px}

.strip{left:0;top:875px;width:946px;height:67px;background:#fbfbfb;border-bottom:2px solid var(--lime)}

.site-footer{left:0;top:942px;width:946px;height:258px;background:var(--footer)}
.social-foot{left:76px;top:44px;display:flex;gap:12px}
.social-foot span{width:24px;height:24px;background:#3f73b8;border-radius:3px}
.social-foot span:last-child{background:#d85a45}
.footer-nav{right:78px;top:49px;display:flex;gap:38px}
.footer-nav a{font-family:"Montserrat",sans-serif;font-size:9.5px;color:#e3e3e3;text-decoration:none}
.copyright{left:74px;top:102px;width:796px;height:38px;background:#d4d4d4;font-size:10px;line-height:38px;padding-left:5px;color:#4a4a4a}
.footer-brand{left:388px;top:174px;display:flex;align-items:center;gap:8px}
.footer-brand .brand-mark{width:24px;height:24px;border-color:#c4c4c4}
.footer-brand .brand-name{color:#c4c4c4;font-size:16px}
.legal{left:0;top:218px;width:946px;text-align:center;font-family:"Montserrat",sans-serif;font-size:10px;color:#a9a9a9}
.legal span{margin:0 12px}
</style>
</head>
<body>

<header class="site-header abs">
  <div class="brand abs"><span class="brand-mark"></span><span class="brand-name">Cedarfield Yard Crew</span></div>
  <div class="social-top abs" aria-label="Social links"><span></span><span></span><span></span><span></span></div>
  <div class="phone abs">0800-555-01-23</div>
</header>

<nav class="main-nav abs">
  <a class="active" href="#">HOME</a>
  <a href="#">SERVICES</a>
  <a href="#">LOCATIONS</a>
  <a href="#">CONSULTANTS</a>
  <a href="#">FAQ</a>
  <a href="#">CONTACT</a>
</nav>

<section class="gallery abs">
  <div class="photo" role="img" aria-label="Lush garden with shrubs and stone steps" style="left:74px;top:0;width:281px;height:101px;background:linear-gradient(135deg,#5e7d3a,#8fb05a)"></div>
  <div class="photo" role="img" aria-label="Monastery courtyard with clipped hedges and bench" style="left:74px;top:108px;width:281px;height:185px;background:linear-gradient(#a9c0d6,#b67a5a 40%,#6f8e45)"></div>
  <div class="photo" role="img" aria-label="Curved lawn edged with pink flower beds by a house" style="left:362px;top:0;width:300px;height:201px;background:linear-gradient(160deg,#d9d4c8,#c85a8a 45%,#5fa532)"></div>
  <div class="promo">
    <div class="l1">DISCOVER</div>
    <div class="l2">A HAPPIER YOU</div>
    <div class="l3">A HAPPIER LAWN</div>
  </div>
  <div class="photo" role="img" aria-label="Flagstone garden path between evergreen shrubs" style="left:670px;top:0;width:200px;height:293px;background:linear-gradient(#4f7a33,#9aa596 60%,#5d8a3a)"></div>
</section>

<div class="slider-dots abs"><span></span><span></span><span></span></div>

<div class="service-btn" style="left:74px">
  <svg width="22" height="22" viewBox="0 0 22 22"><circle cx="5" cy="16" r="3" fill="none" stroke="#3a6a10" stroke-width="2"/><circle cx="5" cy="6" r="3" fill="none" stroke="#3a6a10" stroke-width="2"/><path d="M7 14L20 5M7 8l13 9" stroke="#3a6a10" stroke-width="2"/></svg>
  MAINTENANCE</div>

<div class="service-btn" style="left:344px">
  <svg width="24" height="22" viewBox="0 0 24 22"><path d="M4 22L2 4M9 22L8 2M14 22l2-18M19 22l4-14" stroke="#3a6a10" stroke-width="2.5"/></svg>
  FERTILIZER</div>

<div class="service-btn" style="left:618px;padding-left:20px">
  <svg width="26" height="26" viewBox="0 0 26 26"><circle cx="13" cy="13" r="12" fill="none" stroke="#3a6a10" stroke-width="2"/><ellipse cx="13" cy="14" rx="4" ry="6" fill="#3a6a10"/></svg>
  PEST CONTROL</div>

<section class="about abs">
  <h1>Ut wisi enim ad minim veniam</h1>
  <p style="top:85px">Lorem ipsum dolor sit amet, consectetuer adipiscing elit, sed diam nonummy nibh euismod tincidunt ut laoreet dolore magna aliquam erat volutpat. Ut wisi enim ad minim veniam, quis nostrud exerci tation ullamcorper suscipit lobortis nisl ut aliquip ex ea commodo consequat. Duis autem vel eum iriure dolor in hendrerit in vulputate velit esse molestie consequat, vel illum dolore eu feugiat nulla facilisis at vero eros et accumsan et iusto odio dignissim qui blandit praesent luptatum zzril delenit augue duis dolore te feugait nulla facilisi.</p>
  <p style="top:176px"><b>Consectetuer adipiscing elit</b>, sed diam nonummy nibh euismod tincidunt ut laoreet dolore magna aliquam erat volutpat. Ut wisi enim ad minim veniam, quis nostrud exerci tation ullamcorper suscipit lobortis nisl ut aliquip ex ea commodo consequat. Duis autem vel eum iriure dolor in hendrerit in vulputate.</p>
</section>

<div class="strip abs" role="img" aria-label="Light patterned strip with a person mowing the lawn at the right"></div>

<form class="contact-card abs">
  <h2>CONTACT US</h2>
  <span class="field">NAME</span>
  <span class="field">LAST NAME</span>
  <span class="field">E-MAIL ADDRESS</span>
  <span class="submit">SUBMIT NOW</span>
</form>

<footer class="site-footer abs">
  <div class="social-foot abs" aria-label="Social links"><span></span><span></span><span></span><span></span></div>
  <nav class="footer-nav abs">
    <a href="#">HOME</a><a href="#">SERVICES</a><a href="#">LOCATIONS</a><a href="#">CONSULTANTS</a><a href="#">FAQ</a><a href="#">CONTACT</a>
  </nav>
  <div class="copyright abs">© 2014 Cedarfield Yard Crew.com,</div>
  <div class="footer-brand abs"><span class="brand-mark"></span><span class="brand-name">Cedarfield Yard Crew</span></div>
  <div class="legal abs"><span>LEGAL</span>.<span>PRIVACY POLICY</span>.<span>CONSUMER ACCESS</span>.<span>EMPLOYMENT OPPORTUNITY</span></div>
</footer>

</body>
</html>
```